Stationery design for software development / consultancy company

We need stationary design based on company logo.

We are based in London, UK and we are providing integration solutions development / consultancy services for VEQ integration projects across UK.

Our name refers two words - integration and grace - and it shows our clients our main specialization field and key characteristics of our solutions / products. We also would like to be associated with follow words: smart, reliable, unique.

Project delivery should include:
- Powerpoint template (needs to have a Cover Page, Table of Contents, 1-2 sample pages, and a Closing/Summary slide at the end)
- Letterhead A4 (Word template)
- Standard invoice A4 (Word template)
- With Compliments Slips A5 (Word template)
- Business card (adobe illustrator)

Attached is logo in vector (please use logo with white background!) and company details for printed stationery.

highly skilled IT professionals

Software

• Clear background in all A4/A5 documents.
All text should be editable, i.e. I will need sources.
• I would prefer light, web 2.0 style colours, follow are in my main interest:
- combination of light grey and orange
- Logo colours
• Please no watermarks on printed stationary

```html
<!DOCTYPE html>
<html lang="en">
<head>
<meta charset="utf-8">
<title>Corvanta Invoice</title>
<link rel="stylesheet" href="https://fonts.googleapis.com/css2?family=Arimo:ital,wght@0,400;0,700;1,400&family=Open+Sans:wght@400;700&display=swap">
<style>
  :root {
    --canvas: #e9ebec;
    --paper: #ffffff;
    --ink: #1c1c1c;
    --ink-soft: #555a5e;
    --brand-grey: #4a4f54;
    --brand-orange: #f39200;
    --brand-red: #d9431e;
    --brand-blue: #2aa3dc;
    --rule: #9a9a9a;
    --rule-light: #cfcfcf;
    --fill-yellow: #fdf8c6;
  }
  html, body {
    margin: 0;
    width: 1168px;
    height: 1200px;
    overflow: hidden;
    background: var(--canvas);
  }
  .invoice-sheet {
    position: absolute;
    left: 175px;
    top: 20px;
    width: 819px;
    height: 1160px;
    background: var(--paper);
    box-shadow: 0 1px 3px rgba(0,0,0,.12);
  }
  .invoice-sheet svg { display: block; }
  .wordmark { font-family: "Open Sans", sans-serif; font-weight: 700; font-size: 40px; fill: var(--brand-grey); }
  .company-name { font-family: "Open Sans", sans-serif; font-size: 14px; fill: var(--brand-red); }
  .company-address { font-family: "Open Sans", sans-serif; font-size: 11.5px; fill: var(--ink-soft); }
  .doc-title { font-family: "Arimo", sans-serif; font-weight: 700; font-size: 23px; fill: var(--brand-grey); letter-spacing: .5px; }
  .section-label { font-family: "Arimo", sans-serif; font-weight: 700; font-size: 11.5px; fill: var(--ink); }
  .field-label { font-family: "Arimo", sans-serif; font-size: 11.5px; fill: var(--ink); }
  .field-value { font-family: "Arimo", sans-serif; font-size: 11.5px; fill: var(--ink); }
  .col-head { font-family: "Arimo", sans-serif; font-weight: 700; font-size: 11.5px; fill: var(--ink); }
  .grand-total { font-family: "Arimo", sans-serif; font-weight: 700; font-size: 13px; fill: var(--ink); }
  .thanks { font-family: "Arimo", sans-serif; font-style: italic; font-size: 12.5px; fill: var(--ink); }
  .rule { stroke: var(--rule); stroke-width: 1; fill: none; }
  .rule-light { stroke: var(--rule-light); stroke-width: 1; fill: none; }
  .rule-strong { stroke: var(--ink); stroke-width: 1.4; fill: none; }
  .rule-orange { stroke: var(--brand-orange); stroke-width: 2.4; fill: none; }
  .band-blue { fill: var(--brand-blue); }
  .cell-yellow { fill: var(--fill-yellow); }
</style>
</head>
<body>
<main class="invoice-sheet">
  <svg width="819" height="1160" viewBox="0 0 819 1160" xmlns="http://www.w3.org/2000/svg">
    <!-- Letterhead -->
    <g class="letterhead">
      <circle cx="94" cy="104" r="15" fill="var(--brand-orange)"/>
      <text class="wordmark" x="118" y="118">corvanta</text>
      <text class="company-name" x="77" y="150">Corvanta Limited</text>
      <text class="company-address" x="77" y="170">42 Marlow Court</text>
      <text class="company-address" x="77" y="185">118 Fenwick Lane - London</text>
      <text class="company-address" x="77" y="200">SE9 4RT - United Kingdom</text>
    </g>

    <!-- Title tab -->
    <g class="title-tab">
      <path class="rule-orange" d="M81 216 H632 V177 H738 V216"/>
      <line class="rule" x1="81" y1="222" x2="738" y2="222"/>
      <text class="doc-title" x="640" y="208">INVOICE</text>
    </g>

    <!-- Customer block -->
    <g class="customer-block">
      <path class="rule-strong" d="M81 274 H150 V254 H501"/>
      <text class="section-label" x="81" y="270">Customer</text>
      <text class="field-label" x="89" y="297">Name</text>
      <text class="field-label" x="89" y="314">Attn:</text>
      <text class="field-label" x="89" y="334">Address</text>
      <text class="field-label" x="89" y="353">Suite</text>
      <text class="field-label" x="89" y="372">City</text>
      <text class="field-label" x="89" y="393">Country</text>
      <line class="rule-light" x1="152" y1="301" x2="501" y2="301"/>
      <line class="rule-light" x1="152" y1="320" x2="501" y2="320"/>
      <line class="rule-light" x1="152" y1="337" x2="501" y2="337"/>
      <line class="rule-light" x1="152" y1="395" x2="501" y2="395"/>
    </g>

    <!-- Misc block -->
    <g class="misc-block">
      <path class="rule-strong" d="M568 274 H632 V254 H738 V293"/>
      <text class="section-label" x="570" y="270">Misc</text>
      <text class="field-label" x="570" y="286">Date</text>
      <text class="field-label" x="570" y="325">Order No.</text>
      <text class="field-label" x="570" y="386">Rep</text>
      <text class="field-label" x="570" y="404">FOB</text>
      <line class="rule-light" x1="624" y1="291" x2="738" y2="291"/>
      <line class="rule-light" x1="624" y1="310" x2="738" y2="310"/>
      <line class="rule-light" x1="624" y1="331" x2="738" y2="331"/>
      <line class="rule-light" x1="624" y1="350" x2="738" y2="350"/>
      <line class="rule-light" x1="624" y1="372" x2="738" y2="372"/>
      <line class="rule-light" x1="624" y1="390" x2="738" y2="390"/>
      <line class="rule-light" x1="624" y1="407" x2="738" y2="407"/>
      <text class="field-value" x="680" y="384" text-anchor="middle">JT</text>
    </g>

    <!-- Line items table -->
    <g class="items-table">
      <rect class="cell-yellow" x="638" y="460" width="104" height="322"/>
      <line class="rule" x1="81" y1="441" x2="742" y2="441"/>
      <line class="rule" x1="81" y1="460" x2="742" y2="460"/>
      <line class="rule-light" x1="81" y1="441" x2="81" y2="723"/>
      <line class="rule" x1="154" y1="441" x2="154" y2="723"/>
      <line class="rule" x1="576" y1="441" x2="576" y2="723"/>
      <line class="rule" x1="638" y1="441" x2="638" y2="782"/>
      <line class="rule" x1="742" y1="441" x2="742" y2="796"/>
      <line class="rule-light" x1="638" y1="472" x2="742" y2="472"/>
      <line class="rule-light" x1="638" y1="483" x2="742" y2="483"/>
      <line class="rule-light" x1="638" y1="495" x2="742" y2="495"/>
      <line class="rule-light" x1="638" y1="506" x2="742" y2="506"/>
      <line class="rule-light" x1="638" y1="518" x2="742" y2="518"/>
      <text class="col-head" x="117" y="455" text-anchor="middle">Qty</text>
      <text class="col-head" x="365" y="455" text-anchor="middle">Description</text>
      <text class="col-head" x="607" y="455" text-anchor="middle">Unit Price</text>
      <text class="col-head" x="690" y="455" text-anchor="middle">TOTAL</text>
    </g>

    <!-- Totals -->
    <g class="totals">
      <rect fill="var(--paper)" x="639" y="740" width="102" height="14"/>
      <line class="rule-light" x1="638" y1="740" x2="742" y2="740"/>
      <line class="rule-light" x1="638" y1="754" x2="742" y2="754"/>
      <line class="rule-light" x1="638" y1="768" x2="742" y2="768"/>
      <text class="field-label" x="632" y="738" text-anchor="end">Subtotal</text>
      <text class="field-label" x="632" y="755" text-anchor="end">Shipping</text>
      <text class="field-label" x="505" y="773">Tax Rate(s)</text>
      <line class="rule-light" x1="576" y1="780" x2="742" y2="780"/>
      <line class="rule-light" x1="576" y1="796" x2="638" y2="796"/>
      <text class="grand-total" x="632" y="810" text-anchor="end">TOTAL</text>
      <rect x="638" y="796" width="104" height="19" fill="var(--fill-yellow)" stroke="var(--ink)" stroke-width="1.2"/>
      <rect x="513" y="819" width="229" height="54" fill="var(--fill-yellow)" stroke="var(--rule-light)" stroke-width="1"/>
      <text class="field-label" x="518" y="833">Office Use Only</text>
    </g>

    <!-- Payment block -->
    <g class="payment-block">
      <path class="rule-strong" d="M81 780 H150 V759 H435 V858"/>
      <text class="section-label" x="81" y="776">Payment</text>
      <text class="field-label" x="89" y="803">Comments</text>
      <text class="field-label" x="143" y="822" text-anchor="end">Name</text>
      <text class="section-label" x="143" y="841" text-anchor="end">CC#</text>
      <text class="field-label" x="143" y="861" text-anchor="end">Expires</text>
      <line class="rule-light" x1="143" y1="808" x2="389" y2="808"/>
      <line class="rule-light" x1="143" y1="827" x2="389" y2="827"/>
      <line class="rule-light" x1="143" y1="846" x2="389" y2="846"/>
      <line class="rule-light" x1="143" y1="866" x2="389" y2="866"/>
    </g>

    <!-- Notes box and footer -->
    <rect class="rule-light" x="81" y="896" width="655" height="62"/>
    <g class="footer">
      <rect class="band-blue" x="81" y="987" width="657" height="5"/>
      <line class="rule" x1="81" y1="1000" x2="738" y2="1000"/>
      <text class="thanks" x="409" y="1027" text-anchor="middle">THANK YOU FOR YOUR BUSINESS!!!</text>
    </g>
  </svg>
</main>
</body>
</html>
```